Fatigued and Overloaded by COVID Messages? We need original illustrations to show that.

Everywhere you look there are messages about COVID. That is leading many people to feel fatigued and overloaded by the messages.

We surveyed U.S. adults March 20th - 24th, 2020 and measured message fatigue, information overload, perceived repetition, and perceived exaggeration. Here is how participants responded:

When it comes to coronavirus . . .
55% feel exhausted by all the messages.
54% feel overloaded by the amount of information.
51% feel that the messages are repetitive.
47% feel like messages exaggerate how bad it is.

In other words, almost half of U.S. adults show signs of message fatigue, information overload, perceived message repetition, and perceived message exaggeration.

We will continue to survey 400 adults every week for the next 16 weeks. Each time we will measure message fatigue, information overload, perceived repetition, and perceived exaggeration. We expect that it will increase over time.

What are we looking for? We need innovative and original illustrations that attempt to communicate these findings. The illustrations would visualize message fatigue, information overload, perceived message repetition, and perceived message exaggeration.

What sort of visual are we looking for? Our preference is for an original illustration (or set of illustrations). Our preference is for creative and powerful illustrations, but we are also open to the creative and well-executed infographics.

We need these images fast . We will award monetary prizes to the 3 best designs. If we like more than that, then we might purchase more (e.g., in past contests, we have purchased as many as 30 designs).

What we will need:
(1) The illustrations must be original and we will need the photoshop and/or illustrator files for all artwork. (By original, we mean that the illustrations are 100% created by you. Our organization requires that we utilize only original illustrated work. We have had issues with free imagery being pirated and reposted as free. We sidestep that issue by just having everything created.)

(2) The illustration should say, somewhere: "Based on a survey of 400 U.S. adults conducted March 20 - 24th, 2020."

(3) We will have almost 4 months worth of data by the time this is done. In other words, the illustrations might be able to help us present that weekly data.

(4) We have conducted other Artvendo projects. It might be helpful to examine designs we liked in the past. For example, here is another COVID project we just finished:

https://jobs.artvendo-example.com/job/5162048

Target Market(s)

U.S. adults

Requirements
Must have
• Original illustrations. Mobile friendly design. People will view this on their smartphones.
Nice to have
• A design that we can use to communicate the data across time.

```html
<!DOCTYPE html>
<html lang="en">
<head>
<meta charset="utf-8">
<title>Percent of Americans Feeling Fatigued and Overloaded by COVID Messages</title>
<link rel="stylesheet" href="https://fonts.googleapis.com/css2?family=Exo+2:ital,wght@0,900;1,900&family=Oswald:wght@400;500&display=swap">
<style>
  :root {
    --red: #d14f2e;
    --green: #b1b582;
    --green-light: #e3e4cf;
    --brown: #6b3a1a;
    --white: #ffffff;
  }
  * { margin: 0; padding: 0; box-sizing: border-box; }
  html, body { width: 675px; height: 1200px; overflow: hidden; background: var(--white); }
  .poster { position: relative; width: 675px; height: 1200px; background: var(--white); }

  .header {
    position: absolute; left: 0; top: 0; width: 675px; height: 143px;
    background: var(--red); color: var(--white);
    font-family: "Exo 2", sans-serif; font-weight: 900;
    font-size: 22.5px; letter-spacing: 0.5px; text-align: center;
    line-height: 36px; padding-top: 42px;
  }

  .hero-illustration {
    position: absolute; left: 10px; top: 160px; width: 655px; height: 384px;
    background: radial-gradient(ellipse at 50% 55%, #e9e1cf 0%, var(--green-light) 45%, #f6f6ee 100%);
    border-radius: 8px;
  }

  .intro {
    position: absolute; left: 0; top: 566px; width: 675px; text-align: center;
    font-family: "Oswald", sans-serif; font-weight: 400; color: var(--brown);
    font-size: 27px; line-height: 40px; letter-spacing: -0.6px;
  }

  .stat { position: absolute; left: 69px; width: 500px; height: 82px; }
  .stat-pill {
    position: absolute; left: 70px; top: 6px; width: 428px; height: 70px;
    border: 2.5px solid var(--red); border-radius: 35px; background: var(--white);
  }
  .stat-text {
    position: absolute; left: 90px; top: 0; height: 82px; line-height: 82px;
    font-family: "Oswald", sans-serif; font-weight: 500; color: var(--brown);
    font-size: 24px; letter-spacing: -0.4px; white-space: nowrap;
  }
  .stat-value {
    position: absolute; left: 0; top: 0; width: 82px; height: 82px; border-radius: 50%;
    color: var(--white); text-align: center; line-height: 82px;
    font-family: "Oswald", sans-serif; font-weight: 500; font-size: 30px; letter-spacing: -0.5px;
  }
  .stat-value.green { background: var(--green); }
  .stat-value.red { background: var(--red); }

  .summary {
    position: absolute; left: 55px; top: 1039px; width: 551px; height: 137px;
    border: 1.5px solid var(--red); border-radius: 28px;
    font-family: "Exo 2", sans-serif; font-weight: 900; font-style: italic;
    color: var(--red); font-size: 20px; line-height: 29.5px; text-align: center;
    padding-top: 10px;
  }
</style>
</head>
<body>
<main class="poster">
  <header class="header">
    <h1 style="font-size:inherit;font-weight:inherit;">PERCENT OF AMERICANS FEELING<br>FATIGUED AND OVERLOADED BY COVID MESSAGES</h1>
  </header>

  <div class="hero-illustration" role="img" aria-label="Illustration of a tired person at a table holding their head, surrounded by hands with megaphones, speech bubbles and virus shapes"></div>

  <p class="intro">Based on a survey of U.S. adults conducted March 20th - 24th, 2020<br>When it comes to coronavirus . . .</p>

  <section class="stats">
    <div class="stat" style="top:674px;">
      <div class="stat-pill"></div>
      <span class="stat-text">feel exhausted by all the messages.</span>
      <span class="stat-value green">55%</span>
    </div>
    <div class="stat" style="top:759px;">
      <div class="stat-pill"></div>
      <span class="stat-text" style="left:88px;">feel overloaded by the amount of information.</span>
      <span class="stat-value red">54%</span>
    </div>
    <div class="stat" style="top:845px;">
      <div class="stat-pill"></div>
      <span class="stat-text" style="left:88px;">feel that the messages are repetitive.</span>
      <span class="stat-value green">51%</span>
    </div>
    <div class="stat" style="top:930px;">
      <div class="stat-pill"></div>
      <span class="stat-text" style="left:88px;">feel like messages exaggerate how bad it is.</span>
      <span class="stat-value red">47%</span>
    </div>
  </section>

  <p class="summary">almost half of U.S. adults show signs of<br>message fatigue, information overload,<br>perceived message repetition,<br>and perceived message exaggeration.</p>
</main>
</body>
</html>
```